Marketing company needs business card design

Our company (Ventures Beyond Harbor) need a business card design for a marketing company. The design should of course include the logo and business colors (orange and blue). I would like the design to be clean and professional. The business card is going to be a die cut card that is leaf shaped (I have uploaded the template for it). I would love to see a design that is professional but nothing too "corporate."
Updates

Hello everyone,

Just wanted to let you know that I have uploaded an AI and EPS version of the logo for your convenience.

Thank you!

~Marlene

Industry/Entity Type

Marketing

Requirements
Must have
• Must have the following contact info:

Ventures Beyond Harbor
2817 Hollow Brook Ln B204
Prescott, AZ 86517

928.471.6083

info@venturesbeyondharbor-example.com

```html
<!DOCTYPE html>
<html lang="en">
<head>
<meta charset="utf-8">
<title>Ventures Beyond Harbor – Business Card</title>
<link rel="stylesheet" href="https://fonts.googleapis.com/css2?family=Arimo:wght@400;700&display=swap">
<style>
  :root {
    --page-bg: #e9ecef;
    --brand-blue: #1f9ad6;
    --brand-blue-light: #45b8ec;
    --brand-blue-dark: #137fb8;
    --brand-orange: #e8893a;
    --card-white: #ffffff;
    --text-light: #ffffff;
  }
  html, body {
    margin: 0;
    padding: 0;
    width: 1181px;
    height: 1200px;
    overflow: hidden;
    background: var(--page-bg);
    font-family: "Arimo", Arial, sans-serif;
  }
  .canvas {
    position: relative;
    width: 1181px;
    height: 1200px;
  }
  .card {
    position: absolute;
    left: 90px;
    width: 1000px;
    height: 540px;
    box-sizing: border-box;
    border-radius: 18px 230px 18px 230px;
    box-shadow: 0 10px 30px rgba(0, 0, 0, 0.18);
  }
  .card--front {
    top: 40px;
    background: var(--card-white);
    border: 16px solid var(--brand-blue);
    display: flex;
    align-items: center;
    justify-content: center;
  }
  .brand {
    display: flex;
    align-items: center;
    gap: 18px;
  }
  .brand__dot {
    width: 34px;
    height: 34px;
    border-radius: 50%;
    background: var(--brand-orange);
  }
  .brand__name {
    font-size: 40px;
    font-weight: 400;
    color: var(--brand-blue);
    letter-spacing: 0.5px;
  }
  .card--back {
    top: 620px;
    background: radial-gradient(ellipse at 40% 35%, var(--brand-blue-light) 0%, var(--brand-blue) 60%, var(--brand-blue-dark) 100%);
  }
  .back__mark {
    position: absolute;
    left: 96px;
    top: 270px;
    width: 54px;
    height: 54px;
    border-radius: 50%;
    border: 3px solid var(--text-light);
    box-sizing: border-box;
  }
  .contact {
    position: absolute;
    left: 200px;
    top: 200px;
    color: var(--text-light);
    font-size: 26px;
    line-height: 1.35;
  }
  .contact p { margin: 0; }
  .contact__phone {
    font-weight: 700;
    margin-top: 8px !important;
  }
</style>
</head>
<body>
  <main class="canvas">
    <section class="card card--front" aria-label="Card front">
      <div class="brand">
        <span class="brand__dot"></span>
        <span class="brand__name">Ventures Beyond Harbor</span>
      </div>
    </section>

    <section class="card card--back" aria-label="Card back">
      <span class="back__mark"></span>
      <div class="contact">
        <p>2817 Hollow Brook Ln B204</p>
        <p>Prescott, AZ 86517</p>
        <p class="contact__phone">928.471.6083</p>
        <p>info@venturesbeyondharbor-example.com</p>
      </div>
    </section>
  </main>
</body>
</html>
```